PAQ - 2025

Marlowe Works is a high precision CNC machining company which performs very technical work. Every year we have a theme which is a pillar that drives our production activity. Our theme for 2025 is PAQ
Productivity
Accountability
Quality
We will post these banners in our production areas and lobby.
PAQ should be in large bold orange letters. You can pull photos from my website www.marloweworks-mwi.example and my Instagram account Marlowe Works Inc.

```html
<!DOCTYPE html>
<html lang="en">
<head>
<meta charset="utf-8">
<title>Marlowe Works Inc. — PAQ 2025</title>
<link rel="stylesheet" href="https://fonts.googleapis.com/css2?family=Arvo:wght@700&family=Arimo:ital,wght@1,400&display=swap">
<style>
  :root {
    --paper: #fdfdfd;
    --ink: #2a2a2a;
    --orange: #ee8322;
    --steel-dark: #1e2d4a;
    --steel-mid: #5f7fb0;
    --steel-light: #c9dcef;
  }
  * { margin: 0; padding: 0; box-sizing: border-box; }
  html, body { width: 1200px; height: 2400px; overflow: hidden; }
  body { background: var(--paper); }
  .banner { position: relative; width: 1200px; height: 2400px; background: var(--paper); }

  .brand { position: absolute; top: 0; left: 0; width: 1200px; height: 260px; }
  .brand-name {
    position: absolute; top: 72px; left: 0; width: 1200px;
    display: flex; justify-content: center; align-items: center; gap: 22px;
    font-family: "Arvo", Georgia, serif; font-weight: 700;
    font-size: 78px; line-height: 1; color: var(--ink);
  }
  .brand-dot { width: 58px; height: 58px; border-radius: 50%; background: var(--steel-dark); flex: none; }
  .brand-since {
    position: absolute; top: 170px; left: 826px;
    font-family: "Arimo", Arial, sans-serif; font-size: 15px; color: var(--ink);
  }
  .brand-tagline {
    position: absolute; top: 207px; left: 0; width: 1200px; text-align: center;
    font-family: "Arimo", Arial, sans-serif; font-style: italic;
    font-size: 18px; color: var(--ink);
  }

  .hero-photo {
    position: absolute; top: 260px; left: 0; width: 1200px; height: 898px;
    background:
      radial-gradient(ellipse at 45% 65%, var(--steel-light) 0%, rgba(201,220,239,0) 55%),
      linear-gradient(135deg, var(--steel-mid) 0%, var(--steel-dark) 55%, var(--steel-mid) 100%);
  }

  .type-layer { position: absolute; top: 0; left: 0; width: 1200px; height: 2400px; }
  .theme-mark { font-family: "Arvo", Georgia, serif; font-weight: 700; font-size: 460px; fill: var(--orange); }
  .pillar { font-family: "Arvo", Georgia, serif; font-weight: 700; font-size: 128px; fill: var(--ink); }
  .divider { fill: var(--orange); }
</style>
</head>
<body>
  <main class="banner">
    <header class="brand">
      <div class="brand-name"><span>Marlowe Works Inc.</span><span class="brand-dot"></span></div>
      <div class="brand-since">Since1978</div>
      <p class="brand-tagline">"A complete CNC machining company" Swiss turning, 5 axis milling, CNC turning</p>
    </header>

    <div class="hero-photo" role="img" aria-label="Photo of a coordinate measuring probe touching a machined aluminium housing, in cool blue light"></div>

    <svg class="type-layer" width="1200" height="2400" viewBox="0 0 1200 2400">
      <title>PAQ — Productivity, Accountability, Quality</title>
      <text class="theme-mark" x="63" y="1520" textLength="1076" lengthAdjust="spacingAndGlyphs">PAQ</text>
      <text class="pillar" x="194" y="1769" textLength="815" lengthAdjust="spacingAndGlyphs">Productivity</text>
      <rect class="divider" x="76" y="1825" width="1048" height="3"/>
      <text class="pillar" x="114" y="1981" textLength="973" lengthAdjust="spacingAndGlyphs">Accountability</text>
      <rect class="divider" x="76" y="2047" width="1048" height="3"/>
      <text class="pillar" x="356" y="2187" textLength="494" lengthAdjust="spacingAndGlyphs">Quality</text>
    </svg>
  </main>
</body>
</html>
```